Boutique custom software development company needs new business card

Our nearly 20 year old custom software development company would like to better include the fact that we are now providing Bitcoin services. These new services are B2B include education (how to acquire and securely hold Bitcoin) and integrating Bitcoin payments into existing ecommerce sites or other existing systems. Please keep the card clean and simple. Attached is our current design and some other files. vexalon.example

Target Market(s)

businesses owners interested in long term relationship

Industry/Entity Type

Custom software development and Bitcoin

Contact Information for Business Card

Marcus Ellwood, marcus@vexalon.example, vexalon.example, (888) 555-VEXAL

Font styles to use
Other font styles liked:
• monospace

Requirements
Must have
• double-sided
Nice to have
• clean and simple
Should not have
• physical address

```html
<!DOCTYPE html>
<html lang="en">
<head>
<meta charset="utf-8">
<title>Vexalon Business Card</title>
<link href="https://fonts.googleapis.com/css2?family=Open+Sans:wght@400;700&family=Roboto+Mono:wght@400;700&display=swap" rel="stylesheet">
<style>
  :root {
    --stage: #1e1e1e;
    --brand-blue: #3d72bd;
    --brand-orange: #f07b1f;
    --card-white: #ffffff;
    --ink-grey: #3a3a3a;
  }
  * { margin: 0; padding: 0; box-sizing: border-box; }
  html, body { width: 1200px; height: 801px; overflow: hidden; background: var(--stage); }
  .stage { position: relative; width: 1200px; height: 801px; }

  .card {
    position: absolute;
    width: 520px;
    height: 298px;
    border-radius: 18px;
    overflow: hidden;
  }

  /* Front side */
  .card-front { left: 110px; top: 80px; background: var(--brand-blue); color: var(--card-white); }
  .card-front .brand { position: absolute; left: 120px; top: 78px; }
  .brand-name {
    display: flex; align-items: center; gap: 12px;
    font-family: "Open Sans", sans-serif; font-weight: 700;
    font-size: 58px; letter-spacing: 1px; line-height: 1;
  }
  .brand-mark { width: 16px; height: 16px; background: var(--brand-orange); flex: none; }
  .brand-tagline {
    font-family: "Open Sans", sans-serif; font-weight: 400;
    font-size: 21px; letter-spacing: -0.5px; margin-top: 8px; padding-left: 28px;
  }
  .services {
    position: absolute; left: 0; right: 0; top: 205px; text-align: center;
    font-family: "Roboto Mono", monospace; font-size: 11.5px; line-height: 1.7; letter-spacing: 0.3px;
  }
  .services .sep { display: inline-block; width: 6px; height: 6px; background: var(--card-white); margin: 0 6px; vertical-align: middle; }

  /* Back side */
  .card-back { left: 580px; top: 420px; background: var(--card-white); }
  .card-back .brand { position: absolute; left: 34px; top: 110px; color: var(--brand-blue); }
  .card-back .brand-name { font-size: 36px; gap: 8px; }
  .card-back .brand-mark { width: 11px; height: 11px; }
  .card-back .brand-tagline { font-size: 13px; padding-left: 19px; margin-top: 5px; }

  .divider { position: absolute; left: 262px; top: 70px; width: 2px; height: 112px; background: var(--brand-orange); }

  .contact { position: absolute; left: 284px; top: 74px; }
  .contact-name {
    font-family: "Roboto Mono", monospace; font-weight: 700;
    font-size: 20px; color: var(--brand-blue); letter-spacing: 0.5px; text-transform: uppercase;
  }
  .contact-list { list-style: none; margin-top: 10px; }
  .contact-list li {
    display: flex; align-items: center; gap: 8px;
    font-family: "Roboto Mono", monospace; font-size: 11.5px; color: var(--ink-grey); line-height: 22px;
  }
  .contact-list svg { width: 12px; height: 12px; flex: none; fill: var(--brand-blue); }

  .band { position: absolute; bottom: 0; left: 0; width: 100%; height: 14px; }
</style>
</head>
<body>
<main class="stage">

  <section class="card card-front" aria-label="Card front">
    <div class="brand">
      <div class="brand-name"><span class="brand-mark"></span>VEXALON</div>
      <div class="brand-tagline">developer of custom applications</div>
    </div>
    <div class="services">
      <div>WEB &amp; NATIVE APPLICATIONS<span class="sep"></span>DIGITAL PROCESS AUTOMATION</div>
      <div>CLOUD-BASED PORTALS<span class="sep"></span>BITCOIN CONSULTING</div>
    </div>
  </section>

  <section class="card card-back" aria-label="Card back">
    <div class="brand">
      <div class="brand-name"><span class="brand-mark"></span>VEXALON</div>
      <div class="brand-tagline">developer of custom applications</div>
    </div>
    <div class="divider"></div>
    <div class="contact">
      <div class="contact-name">Marcus Ellwood</div>
      <ul class="contact-list">
        <li>
          <svg viewBox="0 0 24 24" aria-hidden="true"><path d="M6.6 10.8a15.1 15.1 0 0 0 6.6 6.6l2.2-2.2a1 1 0 0 1 1-.25 11.4 11.4 0 0 0 3.6.57 1 1 0 0 1 1 1V20a1 1 0 0 1-1 1A17 17 0 0 1 3 4a1 1 0 0 1 1-1h3.5a1 1 0 0 1 1 1c0 1.25.2 2.45.57 3.57a1 1 0 0 1-.25 1z"/></svg>
          (888) 555-VEXAL
        </li>
        <li>
          <svg viewBox="0 0 24 24" aria-hidden="true"><path d="M2 5h20v14H2z M2 5l10 8 10-8" fill="none" stroke="#3d72bd" stroke-width="2.4"/></svg>
          marcus@vexalon.example
        </li>
        <li>
          <svg viewBox="0 0 24 24" aria-hidden="true"><circle cx="12" cy="12" r="9.5" fill="none" stroke="#3d72bd" stroke-width="2.4"/><path d="M2.5 12h19M12 2.5c3 3 3 16 0 19M12 2.5c-3 3-3 16 0 19" fill="none" stroke="#3d72bd" stroke-width="1.8"/></svg>
          vexalon.example
        </li>
      </ul>
    </div>
    <svg class="band" viewBox="0 0 520 14" preserveAspectRatio="none" aria-hidden="true">
      <polygon points="0,0 388,0 382,14 0,14" fill="#3d72bd"/>
      <polygon points="394,0 520,0 520,14 388,14" fill="#f07b1f"/>
    </svg>
  </section>

</main>
</body>
</html>
```